Business Card Design Project

Talvor - based in Melbourne, Australia. We plan, design, implement and support network infrastructure (Marden, Dravton, Q7, Sorntail etc).

Target Market(s)

Small/Medium enterprise and Corporate.

Industry/Entity Type

Business

```html
<!DOCTYPE html>
<html lang="en">
<head>
<meta charset="utf-8">
<title>Talvor — Business Card</title>
<link rel="stylesheet" href="https://fonts.googleapis.com/css2?family=Open+Sans:ital,wght@1,700&family=Questrial&display=swap">
<style>
  :root {
    --orange: #d87c28;
    --orange-soft: #efc9a3;
    --grey: #6b6866;
    --white: #ffffff;
    --card-dark: #2b2b2d;
    --card-darker: #1f1f21;
    --stage-top: #ffffff;
    --stage-bottom: #e9b07b;
    --note: #111111;
  }
  * { margin: 0; padding: 0; box-sizing: border-box; }
  html, body { width: 1200px; height: 1000px; overflow: hidden; }
  body {
    position: relative;
    background: linear-gradient(180deg, var(--stage-top) 0%, #f6dcc2 40%, var(--stage-bottom) 100%);
    font-family: "Questrial", "Helvetica Neue", Arial, sans-serif;
  }
  .presenter-note {
    position: absolute; top: 38px; left: 0; width: 1200px;
    text-align: center;
    font-family: "Open Sans", Arial, sans-serif;
    font-style: italic; font-weight: 700; font-size: 20px;
    color: var(--note);
  }
  .card {
    position: absolute; left: 245px; width: 711px; height: 406px;
    overflow: hidden; border: 1px solid #9a9a9a;
  }
  .card--front {
    top: 82px;
    background: linear-gradient(180deg, var(--orange-soft) 0%, #f8ece0 30%, #f7f2ec 50%, var(--orange-soft) 100%);
  }
  .card--back {
    top: 522px;
    background: radial-gradient(ellipse at 50% 50%, var(--card-dark) 0%, var(--card-darker) 100%);
  }
  .card__bg { position: absolute; inset: 0; }
  .wordmark {
    position: absolute; display: flex; align-items: center; gap: 16px;
  }
  .wordmark__dot {
    width: 80px; height: 80px; border-radius: 50%;
    border: 7px solid var(--orange);
  }
  .wordmark__name {
    font-size: 86px; line-height: 1; color: var(--grey); letter-spacing: -1px;
  }
  .card--front .wordmark { left: 150px; top: 84px; }
  .card--back .wordmark { left: 150px; top: 152px; }
  .tagline {
    position: absolute; left: 256px; top: 158px;
    font-size: 21px; color: var(--orange); letter-spacing: 0.5px; word-spacing: 4px;
  }
  .contact-band { position: absolute; left: 0; top: 287px; }
  .address, .contact {
    position: absolute; color: var(--white); font-size: 20px; line-height: 25px;
  }
  .address { left: 41px; top: 302px; }
  .contact { right: 41px; top: 302px; text-align: right; }
  .contact__line { display: flex; justify-content: flex-end; align-items: center; gap: 8px; }
  .contact__icon { width: 18px; height: 18px; }
</style>
</head>
<body>
  <p class="presenter-note">Please share more information as street address, website, phone, email etc.</p>

  <section class="card card--front" aria-label="Business card front">
    <svg class="card__bg" width="711" height="406" viewBox="0 0 711 406">
      <polygon points="0,0 120,0 420,406 300,406" fill="#ffffff" opacity="0.25"/>
      <polygon points="711,60 711,180 470,406 350,406" fill="#ffffff" opacity="0.2"/>
    </svg>
    <div class="wordmark">
      <span class="wordmark__dot"></span>
      <span class="wordmark__name">talvor</span>
    </div>
    <p class="tagline">planning | design | support</p>
    <svg class="contact-band" width="711" height="119" viewBox="0 0 711 119">
      <path d="M0,45 Q6,0 50,0 H660 Q705,0 711,45 V119 H0 Z" fill="var(--orange)"/>
    </svg>
    <p class="address">Street Address<br>Melbourne</p>
    <div class="contact">
      <p class="contact__line">
        <svg class="contact__icon" viewBox="0 0 18 18"><rect x="1" y="4" width="16" height="11" rx="1.5" fill="#fff"/><path d="M1,5 L9,11 L17,5" stroke="#d87c28" stroke-width="1.3" fill="none"/></svg>
        info@talvor.com
      </p>
      <p class="contact__line">
        <svg class="contact__icon" viewBox="0 0 18 18"><path d="M4,1 L7,1 L8,5 L6,7 Q8,11 11,12 L13,10 L17,11 L17,14 Q16,17 13,17 Q2,14 1,4 Q1,1 4,1 Z" fill="#fff"/></svg>
        123.456.7890
      </p>
      <p class="contact__line">www.talvor.com</p>
    </div>
  </section>

  <section class="card card--back" aria-label="Business card back">
    <svg class="card__bg" width="711" height="406" viewBox="0 0 711 406">
      <polygon points="0,0 711,0 355,200" fill="#333335" opacity="0.6"/>
      <polygon points="0,406 711,406 355,206" fill="#18181a" opacity="0.5"/>
      <polygon points="0,40 240,203 0,366" fill="#1a1a1c" opacity="0.6"/>
      <polygon points="711,40 471,203 711,366" fill="#1a1a1c" opacity="0.6"/>
    </svg>
    <div class="wordmark">
      <span class="wordmark__dot"></span>
      <span class="wordmark__name">talvor</span>
    </div>
  </section>
</body>
</html>
```